Painting Contractor Business Card Design

We are looking for a cool, bold, modern, polished, business card design. We are a high-end residential painting contractor. Please incorporate our logo and keep with our green/black color scheme. We are interested in seeing 2-sided and 1-sided options. Thank you very much!

Industry/Entity Type

Business

Contact Information for Business Card

Info for the card:
Dale Ormsby
mobile 206-555-0193
email dale@tallowbrookpainting.net
web www.tallowbrookpainting.net

```html
<!DOCTYPE html>
<html lang="en">
<head>
<meta charset="utf-8">
<title>Tallowbrook Painting — Business Cards</title>
<link rel="stylesheet" href="https://fonts.googleapis.com/css2?family=Open+Sans:wght@400;600;700&display=swap">
<style>
  :root {
    --backdrop: #2a2b2e;
    --card: #ffffff;
    --brand-green: #3aaa49;
    --ink: #1c1c1c;
    --rule-black: #1a1a1a;
  }
  * { box-sizing: border-box; margin: 0; padding: 0; }
  html, body {
    width: 1200px; height: 900px; overflow: hidden;
    background: var(--backdrop);
    font-family: "Open Sans", Arial, sans-serif;
  }
  .canvas { position: relative; width: 1200px; height: 900px; }

  .card {
    position: absolute;
    width: 600px; height: 343px;
    background: var(--card);
    box-shadow: 0 14px 30px rgba(0,0,0,.45);
    overflow: hidden;
  }
  .card--front { left: 80px; top: 80px; }
  .card--back { left: 520px; top: 477px; }

  .band { position: absolute; left: 0; right: 0; height: 22px; background: var(--brand-green); }
  .band--top { top: 0; }
  .band--bottom { bottom: 0; }
  .hairline { position: absolute; left: 0; right: 0; height: 4px; background: var(--rule-black); }
  .hairline--top { top: 28px; }
  .hairline--bottom { bottom: 28px; }

  .wordmark {
    display: flex; align-items: center; gap: 12px;
    font-weight: 700; color: var(--ink);
    letter-spacing: 2px; text-transform: uppercase;
    white-space: nowrap;
  }
  .wordmark__square { width: 34px; height: 34px; background: var(--brand-green); flex: none; }

  .card--front .wordmark {
    position: absolute; left: 0; right: 0; top: 150px;
    justify-content: center; font-size: 28px;
  }

  .card--back .wordmark {
    position: absolute; left: 36px; top: 60px; font-size: 24px;
  }
  .person {
    position: absolute; left: 0; right: 0; top: 122px; text-align: center;
  }
  .person__name { font-size: 26px; font-weight: 700; color: var(--ink); line-height: 1.1; }
  .person__role {
    display: flex; align-items: center; justify-content: center; gap: 10px;
    margin-top: 4px; font-size: 12px; color: var(--brand-green);
  }
  .person__role::before, .person__role::after {
    content: ""; width: 120px; height: 1.5px; background: var(--brand-green);
  }
  .divider {
    position: absolute; left: 120px; right: 120px; top: 205px;
    height: 1.5px; background: var(--brand-green);
  }
  .contact {
    position: absolute; left: 0; right: 0; top: 222px;
    text-align: center; font-size: 15px; line-height: 1.55; color: var(--ink);
  }
  .contact__label { color: var(--brand-green); }
  .contact__sep { color: var(--brand-green); margin: 0 4px; }
</style>
</head>
<body>
<main class="canvas">
  <section class="card card--front" aria-label="Business card, front">
    <div class="band band--top"></div>
    <div class="hairline hairline--top"></div>
    <div class="wordmark"><span class="wordmark__square"></span>Tallowbrook Painting</div>
    <div class="hairline hairline--bottom"></div>
    <div class="band band--bottom"></div>
  </section>

  <section class="card card--back" aria-label="Business card, back">
    <div class="band band--top"></div>
    <div class="hairline hairline--top"></div>
    <div class="wordmark"><span class="wordmark__square"></span>Tallowbrook Painting</div>
    <div class="person">
      <p class="person__name">Dale Ormsby</p>
      <p class="person__role">Owner</p>
    </div>
    <div class="divider"></div>
    <div class="contact">
      <p><span class="contact__label">Mobile:</span> 206-555-0193<span class="contact__sep">|</span><span class="contact__label">Email:</span> dale@tallowbrookpainting.net</p>
      <p><span class="contact__label">Website:</span> www.tallowbrookpainting.net</p>
    </div>
    <div class="hairline hairline--bottom"></div>
    <div class="band band--bottom"></div>
  </section>
</main>
</body>
</html>
```